ARDEVO EV

We need a business card design for a new Luxury golf cart Company Ardevo. We manufacture and sell high end golf carts. We would like to see designs that are high end. I have the logo so really need a nice clean look.

```html
<!DOCTYPE html>
<html lang="en">
<head>
<meta charset="utf-8">
<title>Ardevo EV — Business Card</title>
<link rel="stylesheet" href="https://fonts.googleapis.com/css2?family=Poppins:wght@400;700&family=Russo+One&display=swap">
<style>
  :root {
    --page-bg: #e9e6e6;
    --frost-light: #f4efef;
    --frost-mid: #e6dcdc;
    --card-black: #000000;
    --accent-teal: #0b8a70;
    --accent-bright: #10a584;
    --name-silver: #c9d1cf;
    --text-white: #ffffff;
  }
  * { box-sizing: border-box; margin: 0; padding: 0; }
  html, body {
    width: 1200px;
    height: 900px;
    overflow: hidden;
    background: var(--page-bg);
  }
  .business-card {
    position: absolute;
    left: 100px;
    top: 141px;
    width: 1000px;
    height: 618px;
    background: linear-gradient(160deg, var(--frost-light) 0%, var(--frost-mid) 60%, var(--frost-light) 100%);
    overflow: hidden;
    box-shadow: 0 12px 30px rgba(0,0,0,0.18);
  }
  .card-shapes {
    position: absolute;
    inset: 0;
    width: 100%;
    height: 100%;
  }
  .brand-name {
    position: absolute;
    left: 60px;
    top: 110px;
    width: 362px;
    text-align: center;
    font-family: "Poppins", sans-serif;
    font-weight: 700;
    font-size: 66px;
    line-height: 96px;
    letter-spacing: 4px;
    color: var(--accent-teal);
  }
  .contact-block {
    position: absolute;
    left: 545px;
    top: 106px;
    color: var(--text-white);
    font-family: "Poppins", sans-serif;
    font-weight: 400;
  }
  .person-name {
    font-family: "Russo One", sans-serif;
    font-weight: 400;
    font-size: 44px;
    line-height: 50px;
    letter-spacing: 1px;
    white-space: nowrap;
    background: linear-gradient(90deg, var(--accent-bright) 0%, var(--accent-teal) 45%, var(--name-silver) 75%, #ffffff 100%);
    -webkit-background-clip: text;
    background-clip: text;
    color: transparent;
  }
  .person-role {
    font-size: 30px;
    line-height: 36px;
    margin-top: -6px;
  }
  .address {
    margin-top: 38px;
    font-size: 30px;
    line-height: 37px;
  }
  .contact-list {
    list-style: none;
    margin-top: 36px;
    font-size: 30px;
    line-height: 37px;
  }
  .contact-list li {
    display: flex;
    align-items: center;
    gap: 8px;
    white-space: nowrap;
  }
  .contact-icon {
    width: 26px;
    height: 26px;
    flex: none;
  }
</style>
</head>
<body>
  <div class="business-card">
    <svg class="card-shapes" viewBox="0 0 1090 673" preserveAspectRatio="none" aria-hidden="true">
      <path class="accent-wave" fill="var(--accent-teal)"
        d="M479,0 L524,0 C565,60 565,150 535,250 C515,315 495,360 475,410 C492,330 512,260 514,195 C517,120 505,60 479,0 Z"/>
      <path class="dark-panel" fill="var(--card-black)"
        d="M524,0 C565,60 565,150 535,250 C505,350 462,420 462,520 C462,600 485,645 500,673 L1090,673 L1090,0 Z"/>
    </svg>

    <div class="brand-name">ARDEVO</div>

    <div class="contact-block">
      <h1 class="person-name">MARCUS HOLLAND</h1>
      <p class="person-role">Managing Director</p>
      <p class="address">421, Address line<br>goes here<br>45452,Country Name</p>
      <ul class="contact-list">
        <li>
          <svg class="contact-icon" viewBox="0 0 24 24" aria-hidden="true">
            <path fill="none" stroke="#fff" stroke-width="1.8" stroke-linejoin="round"
              d="M6.5 3.5l3 3.5-2 2.2c1.2 2.6 3 4.4 5.4 5.5l2.2-2 3.4 3-1.8 3.2C10.5 18.5 5.5 13.5 3.6 5.4z"/>
            <path fill="none" stroke="#fff" stroke-width="1.6" d="M14 4.5a6 6 0 0 1 5.5 5.5M14 8a2.6 2.6 0 0 1 2 2"/>
          </svg>
          <span>021-555 018 642</span>
        </li>
        <li>
          <svg class="contact-icon" viewBox="0 0 24 24" aria-hidden="true">
            <rect x="2" y="5" width="20" height="14" fill="#fff"/>
            <path fill="none" stroke="#000" stroke-width="1.4" d="M2.5 5.5l9.5 7 9.5-7M2.5 18.5l7-6M21.5 18.5l-7-6"/>
          </svg>
          <span>info@ardevoev.com</span>
        </li>
        <li>
          <svg class="contact-icon" viewBox="0 0 24 24" aria-hidden="true">
            <g fill="none" stroke="#fff" stroke-width="1.5">
              <circle cx="12" cy="12" r="9.5"/>
              <ellipse cx="12" cy="12" rx="4.2" ry="9.5"/>
              <path d="M2.5 12h19M4 7h16M4 17h16"/>
            </g>
          </svg>
          <span>www.ardevocarts.com</span>
        </li>
      </ul>
    </div>
  </div>
</body>
</html>
```